Rack Card Design for an Ayurvedic Beauty Product Project

Hello, I need to have rack cards. The rack cards would be about 3 products we are showcasing at an event. I am a cosmetic company. I have a logo and basic design ideas. I have attached some product images and info. By no means am I a designer so please excuse my messy AI files. Please feel free to design this as feminine as you like. :)

Target Market(s)

Beauty industry, organic, holistic, ayurveda

Industry/Entity Type

Cosmetic

```html
<!DOCTYPE html>
<html lang="en">
<head>
<meta charset="utf-8">
<title>Velvet Lotus Rack Cards</title>
<link href="https://fonts.googleapis.com/css2?family=Oswald:wght@300;400&family=Lato:wght@400;700&family=Great+Vibes&family=Montserrat:wght@600&display=swap" rel="stylesheet">
<style>
  :root{
    --bg:#e6e6e6;
    --plum:#a8387a;
    --plum-deep:#8c2462;
    --gold:#e9c98a;
    --gold-deep:#b88a4c;
    --orange:#e68a2a;
    --white:#ffffff;
    --ink-light:#fbeef6;
  }
  *{box-sizing:border-box;margin:0;padding:0}
  html,body{width:1200px;height:1200px;overflow:hidden;background:var(--bg)}
  .stage{position:relative;width:1200px;height:1200px}
  .rack-card{position:absolute;top:248px;width:324px;height:704px;overflow:hidden;background:var(--plum);box-shadow:0 6px 18px rgba(0,0,0,.18)}
  .rack-card--toner{left:68px}
  .rack-card--cream{left:438px}
  .rack-card--serum{left:808px}
  .card-art{position:absolute;inset:0;width:324px;height:704px}
  .brand{position:absolute;left:26px;top:28px;width:110px;text-align:center}
  .brand-dot{display:block;width:62px;height:62px;margin:0 auto 14px;border-radius:50%;background:var(--gold-deep)}
  .brand-name{font-family:"Montserrat",sans-serif;font-weight:600;font-size:12px;letter-spacing:.5px;color:var(--gold-deep);white-space:nowrap}
  .info{position:absolute;left:148px;top:458px;width:160px;color:var(--ink-light)}
  .rack-card--cream .info{top:464px}
  .info-title{font-family:"Oswald",sans-serif;font-weight:300;font-size:14.5px;letter-spacing:-.3px;color:var(--gold);white-space:nowrap;line-height:1.1;margin-bottom:7px}
  .info-body{font-family:"Lato",sans-serif;font-size:6.6px;line-height:8.8px;text-align:justify;hyphens:auto}
  .script-name{font-family:"Great Vibes",cursive;font-size:25px;color:var(--gold);line-height:1;margin-top:10px}
  .script-product{font-family:"Great Vibes",cursive;font-size:11.5px;color:var(--white);margin:3px 0 4px;white-space:nowrap}
  .product-note{font-family:"Lato",sans-serif;font-size:6.6px;line-height:8.8px;text-align:justify}
  .site{font-family:"Lato",sans-serif;font-size:6.6px;letter-spacing:1.2px;margin-top:7px;color:var(--white)}
</style>
</head>
<body>
<main class="stage">

  <svg width="0" height="0" style="position:absolute" aria-hidden="true">
    <defs>
      <linearGradient id="plumFade" x1="0" y1="0" x2="0" y2="1">
        <stop offset="0" stop-color="#8c2462"/>
        <stop offset="1" stop-color="#b2468a"/>
      </linearGradient>
      <radialGradient id="portraitTone" cx="0.55" cy="0.45" r="0.6">
        <stop offset="0" stop-color="#f1d3c4"/>
        <stop offset="0.6" stop-color="#f8e6dc"/>
        <stop offset="1" stop-color="#ffffff"/>
      </radialGradient>
      <linearGradient id="tubeTone" x1="0" y1="0" x2="0" y2="1">
        <stop offset="0" stop-color="#7d2160"/>
        <stop offset="0.8" stop-color="#a13b7c"/>
        <stop offset="1" stop-color="#c9a462"/>
      </linearGradient>
      <linearGradient id="jarTone" x1="0" y1="0" x2="0" y2="1">
        <stop offset="0" stop-color="#d8b878"/>
        <stop offset="0.2" stop-color="#f4f2f3"/>
        <stop offset="1" stop-color="#e4dde1"/>
      </linearGradient>
      <symbol id="cardBackdrop" viewBox="0 0 324 704">
        <rect width="324" height="704" fill="url(#plumFade)"/>
        <path d="M0 0 H238 C256 22 292 34 324 20 V150 C300 170 290 230 300 280 C310 330 324 350 324 372 V440 C304 446 282 470 258 456 C232 440 214 448 190 440 C160 430 132 448 110 430 C88 412 66 410 62 386 C68 344 96 320 88 282 C80 236 44 196 0 184 Z" fill="var(--white)"/>
        <path d="M0 146 C40 154 64 178 72 210" fill="none" stroke="var(--orange)" stroke-width="3"/>
        <path d="M56 360 C80 392 112 400 150 410 C190 420 230 414 262 404" fill="none" stroke="var(--orange)" stroke-width="1.6" opacity=".85"/>
      </symbol>
    </defs>
  </svg>

  <article class="rack-card rack-card--toner">
    <svg class="card-art" viewBox="0 0 324 704" aria-hidden="true"><use href="#cardBackdrop"/></svg>
    <svg class="card-art" viewBox="0 0 324 704">
      <g role="img" aria-label="Portrait of a woman with her hands framing her face">
        <path d="M118 92 C170 70 250 80 290 150 C310 220 300 300 318 360 C300 420 250 450 190 436 C140 424 100 420 80 390 C96 330 120 300 110 250 C104 190 96 130 118 92 Z" fill="url(#portraitTone)"/>
      </g>
      <g role="img" aria-label="Product photo of two plum toner tubes with gold caps">
        <rect x="0" y="432" width="138" height="246" rx="8" fill="url(#tubeTone)"/>
      </g>
    </svg>
    <div class="brand"><span class="brand-dot"></span><span class="brand-name">VELVET LOTUS</span></div>
    <div class="info">
      <h2 class="info-title">VELVET LOTUS PRODUCT LIST</h2>
      <p class="info-body">Velvet Lotus curates organic infused products where holistic skin care meets a luxurious experience. Each ingredient is carefully selected; providing Ayurvedic herbs, rich minerals &amp; elements. Stimulating hydration and anti-oxidants to lift, firm and illuminate your skin. We believe in connecting with your inner mantra, stimulating higher vibrations, self-esteem, positive mind and soul. As a brand we work with our experts/suppliers of Ayurveda to ensure that our products meet the quality, wholesome healing that you need.</p>
      <p class="script-name">Velvet Lotus</p>
      <p class="script-product">Firming and Lifting Breast Toner</p>
      <p class="product-note">Using all natural Ayurvedic herbs, our breast toner prepares the area for maximum absorption, giving you the best results and the most invigorating treatment</p>
      <p class="site">www.your website.com</p>
    </div>
  </article>

  <article class="rack-card rack-card--cream">
    <svg class="card-art" viewBox="0 0 324 704" aria-hidden="true"><use href="#cardBackdrop"/></svg>
    <svg class="card-art" viewBox="0 0 324 704">
      <g role="img" aria-label="Portrait of a woman with her hands framing her face">
        <path d="M118 92 C170 70 250 80 290 150 C310 220 300 300 318 360 C300 420 250 450 190 436 C140 424 100 420 80 390 C96 330 120 300 110 250 C104 190 96 130 118 92 Z" fill="url(#portraitTone)"/>
      </g>
      <g role="img" aria-label="Product photo of a white cream jar with a gold lid">
        <rect x="24" y="458" width="92" height="150" rx="12" fill="url(#jarTone)"/>
      </g>
    </svg>
    <div class="brand"><span class="brand-dot"></span><span class="brand-name">VELVET LOTUS</span></div>
    <div class="info">
      <h2 class="info-title">VELVET LOTUS PRODUCT LIST</h2>
      <p class="info-body">Velvet Lotus curates organic infused products where holistic skin care meets a luxurious experience. Each ingredient is carefully selected; providing Ayurvedic herbs, rich minerals &amp; elements. Stimulating hydration and anti-oxidants to lift, firm and illuminate your skin. We believe in connecting with your inner mantra, stimulating higher vibrations, self-esteem, positive mind and soul. As a brand we work with our experts/suppliers of Ayurveda to ensure that our products meet the quality, wholesome healing that you need.</p>
      <p class="script-name">Velvet Lotus</p>
      <p class="script-product">Firming and Lifting Breast Cream</p>
      <p class="product-note">Velvet Lotus Firming and Lifting Breast Cream Using all natural Ayurvedic herbs, our breast cream helps enhance, tighten, and lift your breast</p>
      <p class="site">www.your website.com</p>
    </div>
  </article>

  <article class="rack-card rack-card--serum">
    <svg class="card-art" viewBox="0 0 324 704" aria-hidden="true"><use href="#cardBackdrop"/></svg>
    <svg class="card-art" viewBox="0 0 324 704">
      <g role="img" aria-label="Portrait of a woman with her hands framing her face">
        <path d="M118 92 C170 70 250 80 290 150 C310 220 300 300 318 360 C300 420 250 450 190 436 C140 424 100 420 80 390 C96 330 120 300 110 250 C104 190 96 130 118 92 Z" fill="url(#portraitTone)"/>
      </g>
      <g role="img" aria-label="Product photo of two plum serum tubes with gold caps">
        <rect x="8" y="436" width="124" height="196" rx="8" fill="url(#tubeTone)"/>
      </g>
    </svg>
    <div class="brand"><span class="brand-dot"></span><span class="brand-name">VELVET LOTUS</span></div>
    <div class="info">
      <h2 class="info-title">VELVET LOTUS PRODUCT LIST</h2>
      <p class="info-body">Velvet Lotus curates organic infused products where holistic skin care meets a luxurious experience. Each ingredient is carefully selected; providing Ayurvedic herbs, rich minerals &amp; elements. Stimulating hydration and anti-oxidants to lift, firm and illuminate your skin. We believe in connecting with your inner mantra, stimulating higher vibrations, self-esteem, positive mind and soul. As a brand we work with our experts/suppliers of Ayurveda to ensure that our products meet the quality, wholesome healing that you need.</p>
      <p class="script-name">Velvet Lotus</p>
      <p class="script-product">Firming and Toning Breast Serum</p>
      <p class="product-note">Using all natural Ayurvedic herbs, and a touch of 24k gold, our serum enhances the experience and quality of results when partnered with the Velvet Lotus Firming and Lifting Breast Cream providing an all-day boosting experience</p>
      <p class="site">www.your website.com</p>
    </div>
  </article>

</main>
</body>
</html>
```